Business Card Design & Logo Design

Im a new company selling: balloons, bespoke gift wrapping services & Christmas decorating services i.e. I will come and decorate your tree, wrap your xmas presents, set & decorate your dining table, help you host your xmas party etc. etc.

I don't do 'cheesey' stuff so need a sophisticated card.

I love b&w colours, I love stripes and smart looking stuff.

I do already have an idea and if I don't find anything else then I will go with my idea but would then just need somebody to create the artwork for me.

www.copperwillow.co.uk is currently in the process of being designed so any ideas of logos/designs must also work with a website.

Industry/Entity Type

Business

Contact Information for Business Card

Copper Willow
Fernley upon Wey
KT14 9RD
Hollowshire
01632 960418
or
07700 900736

treats@copperwillow.co.uk

```html
<!DOCTYPE html>
<html lang="en">
<head>
<meta charset="utf-8">
<title>Copper Willow Fernley – Business Card</title>
<link rel="stylesheet" href="https://fonts.googleapis.com/css2?family=PT+Sans:ital,wght@0,700;1,700&display=swap">
<style>
  :root {
    --card-bg: #000000;
    --ink: #ffffff;
    --accent: #3fa535;
  }
  html, body {
    margin: 0;
    padding: 0;
    width: 1200px;
    height: 720px;
    overflow: hidden;
    background: var(--card-bg);
  }
  .card {
    position: relative;
    width: 1200px;
    height: 720px;
    background: var(--card-bg);
    color: var(--ink);
    font-family: "PT Sans", Arial, sans-serif;
    font-weight: 700;
  }
  .brand-mark {
    position: absolute;
    left: 176px;
    top: 120px;
    width: 62px;
    height: 62px;
    border-radius: 50%;
    background: var(--accent);
  }
  .brand-name {
    position: absolute;
    left: 268px;
    top: 124px;
    margin: 0;
    font-size: 52px;
    line-height: 56px;
    letter-spacing: 6px;
    text-transform: uppercase;
    font-weight: 700;
    white-space: nowrap;
    color: var(--ink);
  }
  .divider {
    position: absolute;
    left: 62px;
    top: 233px;
    width: 1085px;
    height: 2px;
    background: var(--ink);
  }
  .contact-list {
    list-style: none;
    margin: 0;
    padding: 0;
  }
  .contact-item {
    position: absolute;
    left: 106px;
    display: flex;
    align-items: flex-start;
    font-size: 25px;
    line-height: 30px;
    white-space: nowrap;
  }
  .contact-item svg {
    width: 24px;
    height: 24px;
    margin-top: 4px;
    flex: none;
  }
  .contact-item .value { margin-left: 14px; }
  .contact-phone { top: 258px; }
  .contact-email { top: 336px; }
  .contact-web { top: 415px; }
  .contact-address { top: 492px; }
  .contact-address svg { width: 24px; height: 34px; margin-top: 0; }
  .contact-address .value { line-height: 44px; margin-top: -6px; font-style: normal; }
  .services {
    position: absolute;
    left: 806px;
    top: 506px;
    margin: 0;
    padding: 0;
    list-style: none;
    font-style: italic;
    font-variant: small-caps;
    font-size: 24px;
    line-height: 35.5px;
    letter-spacing: 1px;
    word-spacing: 8px;
    white-space: nowrap;
  }
</style>
</head>
<body>
<main class="card">
  <header>
    <span class="brand-mark" aria-hidden="true"></span>
    <h1 class="brand-name">Copper Willow Fernley</h1>
  </header>
  <div class="divider"></div>

  <ul class="contact-list">
    <li class="contact-item contact-phone">
      <svg viewBox="0 0 24 24" aria-hidden="true"><path fill="#fff" d="M6.6 10.8a15.1 15.1 0 0 0 6.6 6.6l2.2-2.2c.3-.3.7-.4 1-.2 1.1.4 2.3.6 3.6.6.6 0 1 .4 1 1V20c0 .6-.4 1-1 1A17 17 0 0 1 3 4c0-.6.4-1 1-1h3.5c.6 0 1 .4 1 1 0 1.3.2 2.5.6 3.6.1.3 0 .7-.2 1z"/></svg>
      <span class="value">01632 960418 / 07700 900736</span>
    </li>
    <li class="contact-item contact-email">
      <svg viewBox="0 0 24 24" aria-hidden="true"><rect x="2" y="5" width="20" height="14" fill="none" stroke="#fff" stroke-width="2"/><path d="M2 5l10 8 10-8M2 19l7-7M22 19l-7-7" fill="none" stroke="#fff" stroke-width="1.6"/></svg>
      <span class="value">treats@copperwillow.co.uk</span>
    </li>
    <li class="contact-item contact-web">
      <svg viewBox="0 0 24 24" aria-hidden="true"><g fill="none" stroke="#fff" stroke-width="1.6"><circle cx="12" cy="12" r="10"/><ellipse cx="12" cy="12" rx="4.5" ry="10"/><path d="M2 12h20M4 7h16M4 17h16"/></g></svg>
      <span class="value">www.copperwillow.co.uk</span>
    </li>
    <li class="contact-item contact-address">
      <svg viewBox="0 0 24 34" aria-hidden="true"><path fill="#fff" fill-rule="evenodd" d="M12 0C5.4 0 0 5.2 0 11.7 0 20.5 12 34 12 34s12-13.5 12-22.3C24 5.2 18.6 0 12 0zm0 16.5a5 5 0 1 1 0-10 5 5 0 0 1 0 10z"/></svg>
      <address class="value">Copper Willow Fernley upon<br>Wey KT14 9RD<br>Hollowshire</address>
    </li>
  </ul>

  <ul class="services">
    <li>- Christmas decorating</li>
    <li>- Gift wrapping services</li>
    <li>- Host your xmas party</li>
  </ul>
</main>
</body>
</html>
```